Professional business card for the wholesale of metals, chemicals and waste

We are an established company in the wholesale trade of metals, chemicals and waste and are looking for a creative, professional design for our business card. The business card should reflect the values of our company - competence, reliability and innovative strength. It should convey both industry expertise and a modern, trustworthy image.
Important information for the design:

Logo: Our company logo must be prominently placed on the business card.
Colors: Please refer to the colors used on our website www.rtx-gmbh.at. These colors should appear in the design to maintain the visual identity of our company.

QR Code: The business card should contain a QR code that contains all the information listed on the business card.
Font: Choose clear, easy-to-read fonts that reflect a modern, professional look.
Layout: The design should be clear and structured so that both text and visual elements (logo, QR code) are in a balanced relationship to each other.

Information that should appear on the business card:

Company name: RTX Handelsagenturen GmbH
Title: Dipl.-Ing.
Name: Lukas Hofstaller
Position: Managing Director of Operations & Corporate Development
Phone: +43 4273 5812 46
Mobile: +43 664 57 39 218
Email: lukas.hofstaller@rtx-gmbh.at
Homepage: www.rtx-gmbh.at

Design style:

Industry: Industrial yet modern style that conveys competence and trust.
Message: The business card should present our company as a leading supplier in the wholesale trade of metals, chemicals and waste – reliable, professional and innovative.
Target group: Our target group consists of B2B customers and industry contacts who are looking for high-quality products and services in the areas of metal trading, chemicals and waste management.

We look forward to creative designs that reflect our professional identity and are also modern and appealing. Your design should make a statement for our company!

```html
<!DOCTYPE html>
<html lang="de">
<head>
<meta charset="utf-8">
<title>Orbenta Handelsagenturen GmbH – Visitenkarte</title>
<link rel="stylesheet" href="https://fonts.googleapis.com/css2?family=Montserrat:wght@400;500;700;800&display=swap">
<style>
  :root {
    --navy: #1f2249;
    --white: #ffffff;
    --stage: #e9e7e4;
    --line: rgba(255,255,255,0.85);
  }
  * { box-sizing: border-box; margin: 0; padding: 0; }
  html, body { width: 1200px; height: 878px; overflow: hidden; }
  body {
    background: var(--stage);
    font-family: "Montserrat", Arial, sans-serif;
    position: relative;
  }
  .card {
    position: absolute;
    top: 139px;
    width: 340px;
    height: 600px;
    overflow: hidden;
    background: var(--navy);
    box-shadow: 0 10px 24px rgba(0,0,0,0.18);
  }
  .card--back { left: 215px; }
  .card--front { left: 645px; color: var(--white); }

  .brand-name {
    position: absolute;
    left: 0; right: 0;
    text-align: center;
    font-weight: 800;
    letter-spacing: 1px;
    line-height: 1;
  }
  .card--back .brand-name { top: 272px; font-size: 58px; color: var(--white); }

  .front-top {
    position: absolute; left: 0; top: 0; width: 100%; height: 232px;
    background: var(--white);
  }
  .company-name {
    position: absolute; left: 28px; top: 30px;
    font-size: 11px; font-weight: 700; color: var(--navy); letter-spacing: 0.2px;
  }
  .card--front .brand-name { top: 128px; font-size: 52px; color: var(--navy); }

  .person { position: absolute; left: 0; right: 0; top: 272px; }
  .rule-row { display: flex; align-items: center; gap: 12px; }
  .rule { flex: 1; height: 1px; background: var(--line); }
  .rule--blank { background: transparent; }
  .person-name { font-size: 19px; font-weight: 800; letter-spacing: 0.6px; white-space: nowrap; }
  .person-degree { font-size: 14px; margin-top: 6px; white-space: nowrap; }
  .person-role { font-size: 14px; line-height: 1.3; margin-top: 8px; text-align: center; }
  .rule--role { width: 260px; height: 1px; background: var(--line); margin: 22px auto 0; }

  .icon-row { position: absolute; top: 412px; left: 0; right: 0; }
  .icons { display: flex; gap: 14px; }
  .icon {
    width: 26px; height: 26px; border-radius: 50%;
    background: var(--white);
    display: flex; align-items: center; justify-content: center;
  }
  .icon svg { width: 15px; height: 15px; }

  .contacts {
    position: absolute; top: 460px; left: 0; right: 0;
    list-style: none; text-align: center;
    font-size: 13px; line-height: 1.55; font-weight: 500;
  }
</style>
</head>
<body>
  <section class="card card--back" aria-label="Kartenrückseite">
    <p class="brand-name">ORBENTA</p>
  </section>

  <section class="card card--front" aria-label="Kartenvorderseite">
    <div class="front-top"></div>
    <p class="company-name">ORBENTA HANDELSAGENTUREN GMBH</p>
    <p class="brand-name">ORBENTA</p>

    <div class="person">
      <div class="rule-row">
        <span class="rule rule--blank"></span>
        <p class="person-name">LUKAS HOFSTALLER</p>
        <span class="rule"></span>
      </div>
      <div class="rule-row">
        <span class="rule"></span>
        <p class="person-degree">Dipl.-Ing.</p>
        <span class="rule"></span>
      </div>
      <p class="person-role">Managing Director of Operations<br>&amp; Corporate Development</p>
      <div class="rule--role"></div>
    </div>

    <div class="icon-row rule-row">
      <span class="rule"></span>
      <div class="icons">
        <span class="icon" aria-label="Telefon">
          <svg viewBox="0 0 16 16"><path fill="#1f2249" d="M2 5c0-1.5 2.5-2.5 6-2.5S14 3.5 14 5v1.2h-3V5H5v1.2H2z M4 7h8l1.5 6h-11z"/></svg>
        </span>
        <span class="icon" aria-label="Mobil">
          <svg viewBox="0 0 16 16"><rect x="4.5" y="1.5" width="7" height="13" rx="1.2" fill="none" stroke="#1f2249" stroke-width="1.4"/><circle cx="8" cy="12.3" r="0.8" fill="#1f2249"/></svg>
        </span>
        <span class="icon" aria-label="E-Mail">
          <svg viewBox="0 0 16 16"><rect x="1.5" y="3.5" width="13" height="9" fill="#1f2249"/><path d="M1.5 3.5 8 9l6.5-5.5" fill="none" stroke="#fff" stroke-width="1"/></svg>
        </span>
        <span class="icon" aria-label="Website">
          <svg viewBox="0 0 16 16"><circle cx="8" cy="8" r="6.2" fill="none" stroke="#1f2249" stroke-width="1.3"/><ellipse cx="8" cy="8" rx="2.6" ry="6.2" fill="none" stroke="#1f2249" stroke-width="1"/><path d="M1.8 8h12.4" stroke="#1f2249" stroke-width="1"/></svg>
        </span>
      </div>
      <span class="rule"></span>
    </div>

    <ul class="contacts">
      <li>+43 4273 5812 46</li>
      <li>+43 664 57 39 218</li>
      <li>lukas.hofstaller@orbenta-gmbh.at</li>
      <li>www.orbenta-gmbh.at</li>
    </ul>
  </section>
</body>
</html>
```